law firm seeking modern professional FB design

We have an existing FB page and wish to have a professional design for it (see FB Marrow Legal). We also have a web site and business cards with a basic logo and want this logo improved or replaced.

We would like the FB page to be eye catching and stand out. The page features advertisements and articles of general interest and we want a design that fits in with the material that is presented.

The business is seeking to attract reasonably affluent clients seeking legal advice and representation in family law matters.

Target Market(s)

legal services offered in family law - target market being people in relationships that have ended for property and parenting disputes/advice.

Industry/Entity Type

Legal

Contact Information for Business Card

see attachment provided for proposed general lay out with logot o be replaced..

Font styles to use
Sans Serif

Colors
0355a3
a54499
b7b7b7
000000
ec1f27
ffc214

Requirements
Must have
• Modern professional looking FB page and logo that fits in with current website design at marrow.legal
Nice to have
• Have open mind about what will work
• *For the business card design it also needs to incorporate a second logo (already designed) that is in teh upload section below.

```html
<!DOCTYPE html>
<html lang="en">
<head>
<meta charset="utf-8">
<title>Marrow Legal – Facebook Design</title>
<link rel="stylesheet" href="https://fonts.googleapis.com/css2?family=Open+Sans:wght@400;600;700&family=Roboto+Condensed:wght@400&display=swap">
<style>
  :root {
    --brand-blue: #0355a3;
    --brand-blue-light: #1c6fc6;
    --brand-red: #ec1f27;
    --brand-red-dark: #b5121a;
    --silver: #e4e5e7;
    --white: #ffffff;
    --ink: #1b2430;
    --photo-top: #5f6d86;
    --photo-mid: #8a6f62;
    --photo-low: #34435e;
    --photo-base: #1e2533;
  }
  * { box-sizing: border-box; margin: 0; padding: 0; }
  html, body { width: 1200px; height: 1200px; overflow: hidden; }
  body {
    background: var(--silver);
    font-family: "Open Sans", Arial, sans-serif;
    position: relative;
  }

  /* Brand wordmark */
  .brand-mark {
    position: absolute;
    left: 282px; top: 88px;
    width: 600px; height: 150px;
    display: flex; align-items: center; gap: 28px;
  }
  .brand-mark__square {
    flex: none;
    width: 110px; height: 110px;
    background: var(--brand-red);
  }
  .brand-mark__name {
    color: var(--brand-red);
    font-weight: 700;
    font-size: 64px;
    letter-spacing: 2px;
    text-transform: uppercase;
    line-height: 1;
    white-space: nowrap;
  }

  /* Banner shared */
  .banner {
    position: absolute;
    overflow: hidden;
    background: var(--ink);
  }
  .banner__photo {
    position: absolute; inset: 0;
    background: linear-gradient(180deg, var(--photo-top) 0%, var(--photo-mid) 40%, var(--photo-low) 65%, var(--photo-base) 100%);
  }
  .banner__panel { position: absolute; inset: 0; width: 100%; height: 100%; }

  .banner__contacts {
    position: absolute;
    list-style: none;
    color: var(--white);
  }
  .banner__contacts li { display: flex; align-items: center; white-space: nowrap; }
  .banner__contacts svg { flex: none; fill: var(--white); }

  .banner__content {
    position: absolute;
    color: var(--white);
    text-align: center;
    display: flex; flex-direction: column; align-items: center;
  }
  .banner__brand {
    font-weight: 700;
    color: var(--white);
    text-transform: uppercase;
    letter-spacing: 2px;
    display: flex; align-items: center;
    white-space: nowrap;
  }
  .banner__brand-square { background: var(--brand-red); }
  .banner__headline {
    font-weight: 700;
    text-transform: uppercase;
    line-height: 1.02;
    white-space: nowrap;
  }
  .banner__services { display: flex; list-style: none; }
  .service-ring {
    border: 2px solid var(--white);
    border-radius: 50%;
    display: flex; align-items: center; justify-content: center;
    text-transform: uppercase;
    line-height: 1.2;
  }
  .banner__region {
    font-weight: 600;
    text-transform: uppercase;
    line-height: 1.75;
    white-space: nowrap;
  }

  /* Small banner */
  .banner--compact { left: 318px; top: 324px; width: 564px; height: 294px; }
  .banner--compact .banner__contacts { left: 12px; top: 12px; font-size: 9.5px; }
  .banner--compact .banner__contacts li { gap: 10px; height: 20px; }
  .banner--compact .banner__contacts svg { width: 12px; height: 12px; }
  .banner--compact .banner__content { left: 270px; right: 0; top: 24px; }
  .banner--compact .banner__brand { font-size: 16px; gap: 6px; }
  .banner--compact .banner__brand-square { width: 14px; height: 14px; }
  .banner--compact .banner__headline { font-size: 22px; margin-top: 22px; }
  .banner--compact .banner__services { gap: 16px; margin-top: 14px; }
  .banner--compact .service-ring { width: 70px; height: 70px; font-size: 8px; }
  .banner--compact .banner__region { font-size: 9.5px; margin-top: 10px; }
  .learn-more {
    position: absolute; left: 14px; top: 248px;
    width: 164px; height: 34px;
    background: linear-gradient(180deg, var(--brand-red) 0%, var(--brand-red-dark) 100%);
    border: 1px solid #f6d0d2;
    color: var(--white);
    font-family: "Roboto Condensed", "Arial Narrow", sans-serif;
    font-size: 21px;
    display: flex; align-items: center; justify-content: center;
    text-transform: uppercase;
  }

  /* Large banner */
  .banner--wide { left: 0; top: 714px; width: 1200px; height: 442px; }
  .banner--wide .banner__contacts { left: 16px; top: 22px; font-size: 17px; }
  .banner--wide .banner__contacts li { gap: 26px; height: 38px; }
  .banner--wide .banner__contacts svg { width: 24px; height: 24px; }
  .banner--wide .banner__content { left: 560px; right: 32px; top: 34px; }
  .banner--wide .banner__brand { font-size: 32px; gap: 12px; }
  .banner--wide .banner__brand-square { width: 28px; height: 28px; }
  .banner--wide .banner__headline { font-size: 56px; margin-top: 36px; }
  .banner--wide .banner__services { gap: 26px; margin-top: 18px; }
  .banner--wide .service-ring { width: 98px; height: 98px; font-size: 12.5px; }
  .banner--wide .banner__region { font-size: 18px; margin-top: 20px; }
</style>
</head>
<body>

  <div class="brand-mark">
    <span class="brand-mark__square"></span>
    <span class="brand-mark__name">Marrow<br>Legal</span>
  </div>

  <!-- Compact cover -->
  <section class="banner banner--compact">
    <div class="banner__photo" role="img" aria-label="Photo of a sunset over the sea with waves breaking on coastal rocks"></div>
    <svg class="banner__panel" viewBox="0 0 564 294" preserveAspectRatio="none" aria-hidden="true">
      <defs>
        <linearGradient id="panelCompact" x1="0" y1="0" x2="1" y2="1">
          <stop offset="0" stop-color="#1c6fc6"/>
          <stop offset="1" stop-color="#0355a3"/>
        </linearGradient>
      </defs>
      <path d="M264,0 Q220,147 282,294" fill="none" stroke="#ec1f27" stroke-width="10"/>
      <path d="M270,0 Q226,147 288,294 L564,294 L564,0 Z" fill="url(#panelCompact)"/>
    </svg>
    <ul class="banner__contacts">
      <li><svg viewBox="0 0 24 24"><path d="M3 8c0-3 4-4 9-4s9 1 9 4v2h-5V8H8v2H3z M6 11h12l2 9H4z"/></svg>(02) 4000 1234</li>
      <li><svg viewBox="0 0 24 24"><path d="M12 2 2 9v13h20V9zM6 12h12v7H6z"/></svg>admin@marrow.legal</li>
      <li><svg viewBox="0 0 24 24"><path d="M12 2a10 10 0 1 0 0 20 10 10 0 0 0 0-20zm0 2c1.2 0 2.6 2.4 3 7H9c.4-4.6 1.8-7 3-7zM4.1 11a8 8 0 0 1 4.5-6.3C7.7 6.4 7.1 8.6 7 11zm0 2H7c.1 2.4.7 4.6 1.6 6.3A8 8 0 0 1 4.1 13zM12 20c-1.2 0-2.6-2.4-3-7h6c-.4 4.6-1.8 7-3 7zm3.4-.7c.9-1.7 1.5-3.9 1.6-6.3h2.9a8 8 0 0 1-4.5 6.3zM17 11c-.1-2.4-.7-4.6-1.6-6.3A8 8 0 0 1 19.9 11z"/></svg>www.marrow.legal</li>
    </ul>
    <div class="banner__content">
      <div class="banner__brand"><span class="banner__brand-square"></span>Marrow Legal</div>
      <h2 class="banner__headline">The Legal Experts<br>in Family Law</h2>
      <ul class="banner__services">
        <li class="service-ring">Parenting<br>Matters</li>
        <li class="service-ring">Property<br>Matters</li>
        <li class="service-ring">Children's<br>Law</li>
      </ul>
      <p class="banner__region">Providing quality legal services to the Illawarra,<br>Southern Highlands and South Coast</p>
    </div>
    <div class="learn-more">Learn More</div>
  </section>

  <!-- Wide cover -->
  <section class="banner banner--wide">
    <div class="banner__photo" role="img" aria-label="Photo of a sunset over the sea with waves breaking on coastal rocks"></div>
    <svg class="banner__panel" viewBox="0 0 1200 442" preserveAspectRatio="none" aria-hidden="true">
      <defs>
        <linearGradient id="panelWide" x1="0" y1="0" x2="1" y2="1">
          <stop offset="0" stop-color="#1c6fc6"/>
          <stop offset="1" stop-color="#0355a3"/>
        </linearGradient>
      </defs>
      <path d="M553,0 Q459,221 565,442" fill="none" stroke="#ec1f27" stroke-width="16"/>
      <path d="M564,0 Q470,221 576,442 L1200,442 L1200,0 Z" fill="url(#panelWide)"/>
    </svg>
    <ul class="banner__contacts">
      <li><svg viewBox="0 0 24 24"><path d="M3 8c0-3 4-4 9-4s9 1 9 4v2h-5V8H8v2H3z M6 11h12l2 9H4z"/></svg>(02) 4000 1234</li>
      <li><svg viewBox="0 0 24 24"><path d="M12 2 2 9v13h20V9zM6 12h12v7H6z"/></svg>admin@marrow.legal</li>
      <li><svg viewBox="0 0 24 24"><path d="M12 2a10 10 0 1 0 0 20 10 10 0 0 0 0-20zm0 2c1.2 0 2.6 2.4 3 7H9c.4-4.6 1.8-7 3-7zM4.1 11a8 8 0 0 1 4.5-6.3C7.7 6.4 7.1 8.6 7 11zm0 2H7c.1 2.4.7 4.6 1.6 6.3A8 8 0 0 1 4.1 13zM12 20c-1.2 0-2.6-2.4-3-7h6c-.4 4.6-1.8 7-3 7zm3.4-.7c.9-1.7 1.5-3.9 1.6-6.3h2.9a8 8 0 0 1-4.5 6.3zM17 11c-.1-2.4-.7-4.6-1.6-6.3A8 8 0 0 1 19.9 11z"/></svg>www.marrow.legal</li>
    </ul>
    <div class="banner__content">
      <div class="banner__brand"><span class="banner__brand-square"></span>Marrow Legal</div>
      <h2 class="banner__headline">The Legal Experts<br>in Family Law</h2>
      <ul class="banner__services">
        <li class="service-ring">Parenting<br>Matters</li>
        <li class="service-ring">Property<br>Matters</li>
        <li class="service-ring">Children's<br>Law</li>
      </ul>
      <p class="banner__region">Providing quality legal services to the Illawarra,<br>Southern Highlands and South Coast</p>
    </div>
  </section>

</body>
</html>
```